Upmarket building and construction company needs signage

Our building company R Voss Construction, needs signage to put up on the side of our vehicle trailers and on site fencing. We are a building company that specialises in residential construction and carpentry .

I will attach our logo and some inspirational pics for site fencing as well as what our trailer looks like .
Other details i would like on the sign are our
( email) rvossconstruction@mailpost.example
(mobile ) 0482 913 640
(website ) rvossconstruction. example.au

Target Market(s)

Home owners looking for a reliable local builder who produces good quality work. I have attached some inspirational pics.

Industry/Entity Type

Building and Construction

Colors

Designer to choose colors to be used in the design.

Requirements
Must have
• Our logo, contact information
Nice to have
• We would like the design to have elements of being Elegant, Serious, Modern, Professional, Masculine, Conservative and Upmarket.

```html
<!DOCTYPE html>
<html lang="en">
<head>
<meta charset="utf-8">
<title>R Voss Construction – Site Sign</title>
<link rel="stylesheet" href="https://fonts.googleapis.com/css2?family=Jost:wght@400;500&display=swap">
<style>
  :root {
    --backdrop: #e9e8e5;
    --sign-white: #ffffff;
    --bronze: #a36c35;
    --charcoal: #333232;
    --brand-grey: #6a6a6a;
    --contact-white: #ffffff;
  }
  html, body {
    margin: 0;
    padding: 0;
    width: 1200px;
    height: 1002px;
    overflow: hidden;
    background: var(--backdrop);
  }
  .canvas {
    position: relative;
    width: 1200px;
    height: 1002px;
  }
  .site-sign {
    position: absolute;
    left: 265px;
    top: 51px;
    width: 670px;
    height: 900px;
    box-shadow: 0 6px 24px rgba(0,0,0,0.12);
  }
  .sign-face { fill: var(--sign-white); }
  .sign-band { fill: var(--bronze); }
  .sign-base { fill: var(--charcoal); }
  .brand-name {
    font-family: "Jost", sans-serif;
    font-weight: 400;
    fill: var(--brand-grey);
  }
  .brand-tagline {
    font-family: "Jost", sans-serif;
    font-weight: 400;
    fill: var(--brand-grey);
    letter-spacing: 1.5px;
  }
  .contact-phone {
    font-family: "Jost", sans-serif;
    font-weight: 500;
    fill: var(--contact-white);
  }
  .contact-email {
    font-family: "Jost", sans-serif;
    font-weight: 400;
    fill: var(--contact-white);
  }
</style>
</head>
<body>
<main class="canvas">
  <svg class="site-sign" viewBox="0 0 638 857" xmlns="http://www.w3.org/2000/svg" aria-label="R Voss Construction site sign">
    <rect class="sign-base" x="0" y="0" width="638" height="857"/>
    <path class="sign-band" d="M0,0 H638 V597 Q300,732 0,567 Z"/>
    <path class="sign-face" d="M0,0 H638 V460 Q290,705 0,527 Z"/>

    <text class="brand-name" x="565" y="377" font-size="104" text-anchor="end" letter-spacing="4">R VOSS</text>
    <text class="brand-name" x="565" y="452" font-size="57" text-anchor="end" letter-spacing="2">CONSTRUCTION</text>
    <text class="brand-tagline" x="565" y="502" font-size="31" text-anchor="end">BUILDING AND CARPENTRY</text>

    <text class="contact-phone" x="319" y="762" font-size="62" text-anchor="middle">+61 482 913 640</text>
    <text class="contact-email" x="319" y="804" font-size="25" text-anchor="middle">rvossconstruction@mailpost.example</text>
  </svg>
</main>
</body>
</html>
```